QMB Vane Works

- Brochure design

Target Market(s)

Granite and Quartz

Font styles to use
Sans Serif

Colors

Designer to choose colors to be used in the design.

Requirements
Must have
• I post the instruction file below
Nice to have
Should not have

```html
<!DOCTYPE html>
<html lang="en">
<head>
<meta charset="utf-8">
<title>QMB Vane Works – Product Catalog Brochure</title>
<link href="https://fonts.googleapis.com/css2?family=Open+Sans:wght@300;400;700&display=swap" rel="stylesheet">
<style>
  :root {
    --bg: #ffffff;
    --ink-light: #ffffff;
    --ink-soft: rgba(255,255,255,0.85);
    --wood-dark: #3a2a20;
    --wood-mid: #6b4a33;
    --cabinet: #3c4047;
    --wall: #c9c3bc;
    --window: #9fb7a4;
    --floor: #8a4a26;
  }
  * { margin: 0; padding: 0; box-sizing: border-box; }
  html, body {
    width: 1200px; height: 900px; overflow: hidden;
    background: var(--bg);
    font-family: "Open Sans", Arial, sans-serif;
  }
  .spread {
    position: absolute; left: 140px; top: 150px;
    width: 920px; height: 596px;
    display: flex;
    box-shadow: 0 14px 40px rgba(0,0,0,0.18);
  }
  .panel {
    position: relative; width: 460px; height: 596px; overflow: hidden;
    color: var(--ink-light);
  }
  .photo { position: absolute; inset: 0; }
  .photo--back {
    background:
      linear-gradient(180deg, rgba(0,0,0,0) 55%, rgba(30,20,14,0.55) 100%),
      linear-gradient(180deg, #7a5a44 0%, var(--wall) 22%, #b9aea4 45%, #8c8a88 60%, var(--cabinet) 75%, var(--wood-mid) 100%);
  }
  .photo--front {
    background:
      linear-gradient(180deg, rgba(0,0,0,0) 50%, rgba(20,16,14,0.6) 100%),
      linear-gradient(100deg, rgba(0,0,0,0) 60%, rgba(160,80,30,0.6) 100%),
      linear-gradient(180deg, #dcd8d0 0%, var(--window) 30%, #b8a98f 48%, var(--cabinet) 62%, #2e2f33 80%, var(--floor) 100%);
  }
  .brand-top {
    position: absolute; left: 40px; top: 26px;
  }
  .brand-top .name { font-size: 26px; font-weight: 400; color: var(--ink-soft); letter-spacing: 1px; }
  .brand-top .tagline { font-size: 9px; color: var(--ink-soft); margin-top: 2px; }

  .back-info {
    position: absolute; left: 200px; top: 340px; width: 240px; text-align: center;
  }
  .back-info .name { font-size: 30px; font-weight: 400; letter-spacing: 1px; }
  .back-info .quality { font-size: 14px; margin-bottom: 8px; }
  .back-info .address { font-size: 12px; line-height: 1.35; }
  .categories {
    position: absolute; font-size: 14px; white-space: nowrap;
  }
  .back-categories { left: 60px; bottom: 80px; }

  .cover-title {
    position: absolute; left: 34px; top: 380px;
  }
  .cover-title .line-1 { font-size: 38px; font-weight: 700; letter-spacing: 0.5px; line-height: 1.05; }
  .cover-title .line-2 { font-size: 38px; font-weight: 300; line-height: 1.1; }
  .front-categories { left: 38px; top: 490px; font-size: 14.5px; }
  .web { position: absolute; right: 40px; top: 528px; font-size: 9px; font-weight: 700; }
  .dot { margin: 0 6px; }
</style>
</head>
<body>
  <main class="spread">
    <section class="panel panel--back">
      <div class="photo photo--back" role="img" aria-label="Rustic kitchen with wood-clad island, concrete countertop, farmhouse sink and black pendant lights"></div>
      <div class="back-info">
        <p class="name">Vane Works</p>
        <p class="quality">Premium Quality</p>
        <p class="address">Harlow Trading Inc.<br>4870 Birch Row<br>Austin, TX 78701<br>512 555 0148<br>www.QMBVANEWORKS.com</p>
      </div>
      <p class="categories back-categories">Pre-fabricate Slabs<span class="dot">•</span>Natural Stone<span class="dot">•</span>Granite<span class="dot">•</span>Quartz</p>
    </section>
    <section class="panel panel--front">
      <div class="photo photo--front" role="img" aria-label="Bright kitchen with dark island, granite countertop, tulips and pendant lamps before large windows"></div>
      <header class="brand-top">
        <p class="name">Vane Works</p>
        <p class="tagline">Naturally Beautiful, Premium Quality</p>
      </header>
      <h1 class="cover-title">
        <span class="line-1">QMB VANE WORKS</span><br>
        <span class="line-2">PRODUCT CATALOG</span>
      </h1>
      <p class="categories front-categories">Pre-fabricate Slabs<span class="dot">•</span>Natural Stone<span class="dot">•</span>Granite<span class="dot">•</span>Quartz</p>
      <p class="web">WWW.QMBVANEWORKS.COM</p>
    </section>
  </main>
</body>
</html>
```